An our door sign really promoting our clinic and services

We have a new sports medicine clinic called HALLCREST SPORTS MEDICINE.
We want to make a really nice external sign at our clinic using a photo of our team we really like. I have attached the photo.
We want to simply include our LOGO and also signs with these slogan options. So we want different signs with these different slogans so we can choose what we really like.
This should be a simple and quite design.

The SLOGANS WE WOULD LIKE TO SEE ON THE SIGN (only one slogan per sign in the drafts)

1. Your Journey. Our Expertise
2. Where better health begins
3. Building the best version of you
4. Your health, in expert hands
5. Reaching new heights in your health
6. Your path to peak performance starts here

I have also included different versions of our logo based on the background and how you set the sign up

So summary
1. Image attached
2. Slogan options we would like to see them all
3. Logo attached (various options based on how you set the background up)
4. Size of sign is 2935mm wide x 1885mm high

```html
<!DOCTYPE html>
<html lang="en">
<head>
<meta charset="utf-8">
<title>Hallcrest Sports Medicine – Sign Drafts</title>
<link href="https://fonts.googleapis.com/css2?family=Anton&display=swap" rel="stylesheet">
<style>
  :root {
    --stage: #b5b5b5;
    --navy: #15184a;
    --cyan: #3fc1e8;
    --sky: #2aa8e0;
    --white: #ffffff;
  }
  * { box-sizing: border-box; margin: 0; padding: 0; }
  html, body { width: 1200px; height: 2700px; overflow: hidden; }
  body { background: var(--stage); position: relative; font-family: "Anton", sans-serif; }

  .sign {
    position: absolute;
    left: 117px;
    width: 964px;
    height: 619px;
    background: var(--navy);
    overflow: hidden;
    box-shadow: 0 3px 8px rgba(0,0,0,0.25);
  }
  .sign--one { top: 211px; }
  .sign--two { top: 1019px; }
  .sign--three { top: 1828px; }

  .sign__art { position: absolute; inset: 0; width: 964px; height: 619px; }

  .brand {
    position: absolute;
    top: 116px;
    display: flex;
    align-items: center;
    gap: 18px;
    color: var(--white);
  }
  .sign--one .brand { left: 80px; }
  .sign--two .brand, .sign--three .brand { left: 115px; }
  .brand__dot {
    width: 56px; height: 56px;
    border-radius: 50%;
    background: var(--cyan);
  }
  .brand__name {
    font-size: 36px;
    line-height: 1;
    letter-spacing: 4px;
  }
  .brand__name span { display: block; font-size: 16px; letter-spacing: 9.4px; margin-top: 6px; }

  .slogan__top, .slogan__bottom {
    position: absolute;
    font-size: 86px;
    line-height: 1;
    color: var(--white);
    transform-origin: left top;
    transform: skewX(-10deg) scaleX(0.9);
    white-space: nowrap;
  }
  .slogan__top em { font-style: normal; color: var(--cyan); }
  .slogan__band {
    position: absolute;
    left: 0;
    height: 93px;
    background: linear-gradient(90deg, var(--cyan) 0%, var(--cyan) 84%, rgba(63,193,232,0) 100%);
  }

  .sign--one .slogan__top { left: 38px; top: 289px; }
  .sign--one .slogan__band { top: 396px; width: 483px; }
  .sign--one .slogan__bottom { left: 30px; top: 399px; }

  .sign--two .slogan__top { left: 46px; top: 270px; }
  .sign--two .slogan__band { top: 380px; width: 518px; }
  .sign--two .slogan__bottom { left: 34px; top: 383px; }

  .sign--three .slogan__top { left: 46px; top: 293px; font-size: 80px; }
  .sign--three .slogan__band { top: 382px; width: 518px; }
  .sign--three .slogan__bottom { left: 30px; top: 385px; }
</style>
</head>
<body>

<section class="sign sign--one">
  <svg class="sign__art" viewBox="0 0 964 619">
    <defs>
      <linearGradient id="swoosh-one" x1="0" y1="0" x2="0.3" y2="1">
        <stop offset="0" stop-color="#1c3f86"/><stop offset="0.45" stop-color="#2a9fd8"/><stop offset="1" stop-color="#4cc8ee"/>
      </linearGradient>
      <linearGradient id="photo-one" x1="0" y1="0" x2="0.4" y2="1">
        <stop offset="0" stop-color="#c9ccd0"/><stop offset="0.4" stop-color="#4a4d56"/><stop offset="0.75" stop-color="#24262e"/><stop offset="1" stop-color="#3f6e3a"/>
      </linearGradient>
    </defs>
    <g class="sign__swoosh">
      <path d="M523 0 L753 0 C620 90 512 200 515 300 C518 420 590 540 673 619 L573 619 C540 520 515 400 501 280 C488 180 495 80 523 0Z" fill="url(#swoosh-one)"/>
      <path d="M640 0 L753 0 C620 90 512 200 515 300 C518 400 560 500 600 560 C540 470 520 380 525 290 C530 180 580 80 640 0Z" fill="#2aa8e0"/>
      <path role="img" aria-label="Photo of two clinic team members reviewing a tablet in the gym" d="M753 0 L964 0 L964 619 L673 619 C590 540 518 420 515 300 C512 200 620 90 753 0Z" fill="url(#photo-one)"/>
      <path d="M853 0 L964 0 L964 29Z" fill="#ffffff"/>
    </g>
  </svg>
  <div class="brand"><div class="brand__dot"></div><div class="brand__name">HALLCREST<span>SPORTS MEDICINE</span></div></div>
  <div class="slogan__top">YOUR <em>JOURNEY</em></div>
  <div class="slogan__band"></div>
  <div class="slogan__bottom">OUR EXPERTISE</div>
</section>

<section class="sign sign--two">
  <svg class="sign__art" viewBox="0 0 964 619">
    <defs>
      <linearGradient id="swoosh-two" x1="0" y1="0" x2="0.3" y2="1">
        <stop offset="0" stop-color="#1c3f86"/><stop offset="0.45" stop-color="#2a9fd8"/><stop offset="1" stop-color="#4cc8ee"/>
      </linearGradient>
      <linearGradient id="photo-two" x1="0" y1="0" x2="0.4" y2="1">
        <stop offset="0" stop-color="#c9ccd0"/><stop offset="0.4" stop-color="#4a4d56"/><stop offset="0.75" stop-color="#24262e"/><stop offset="1" stop-color="#3f6e3a"/>
      </linearGradient>
    </defs>
    <g class="sign__swoosh" transform="translate(35 0)">
      <path d="M523 0 L753 0 C620 90 512 200 515 300 C518 420 590 540 673 619 L573 619 C540 520 515 400 501 280 C488 180 495 80 523 0Z" fill="url(#swoosh-two)"/>
      <path d="M640 0 L753 0 C620 90 512 200 515 300 C518 400 560 500 600 560 C540 470 520 380 525 290 C530 180 580 80 640 0Z" fill="#2aa8e0"/>
      <path role="img" aria-label="Photo of two clinic team members reviewing a tablet in the gym" d="M753 0 L964 0 L964 619 L673 619 C590 540 518 420 515 300 C512 200 620 90 753 0Z" fill="url(#photo-two)"/>
      <path d="M853 0 L964 0 L964 29Z" fill="#ffffff"/>
    </g>
  </svg>
  <div class="brand"><div class="brand__dot"></div><div class="brand__name">HALLCREST<span>SPORTS MEDICINE</span></div></div>
  <div class="slogan__top">WHERE <em>BETTER</em></div>
  <div class="slogan__band"></div>
  <div class="slogan__bottom">HEALTH BEGINS</div>
</section>

<section class="sign sign--three">
  <svg class="sign__art" viewBox="0 0 964 619">
    <defs>
      <linearGradient id="swoosh-three" x1="0" y1="0" x2="0.3" y2="1">
        <stop offset="0" stop-color="#1c3f86"/><stop offset="0.45" stop-color="#2a9fd8"/><stop offset="1" stop-color="#4cc8ee"/>
      </linearGradient>
      <linearGradient id="photo-three" x1="0" y1="0" x2="0.4" y2="1">
        <stop offset="0" stop-color="#c9ccd0"/><stop offset="0.4" stop-color="#4a4d56"/><stop offset="0.75" stop-color="#24262e"/><stop offset="1" stop-color="#3f6e3a"/>
      </linearGradient>
    </defs>
    <g class="sign__swoosh" transform="translate(35 0)">
      <path d="M523 0 L753 0 C620 90 512 200 515 300 C518 420 590 540 673 619 L573 619 C540 520 515 400 501 280 C488 180 495 80 523 0Z" fill="url(#swoosh-three)"/>
      <path d="M640 0 L753 0 C620 90 512 200 515 300 C518 400 560 500 600 560 C540 470 520 380 525 290 C530 180 580 80 640 0Z" fill="#2aa8e0"/>
      <path role="img" aria-label="Photo of two clinic team members reviewing a tablet in the gym" d="M753 0 L964 0 L964 619 L673 619 C590 540 518 420 515 300 C512 200 620 90 753 0Z" fill="url(#photo-three)"/>
      <path d="M853 0 L964 0 L964 29Z" fill="#ffffff"/>
    </g>
  </svg>
  <div class="brand"><div class="brand__dot"></div><div class="brand__name">HALLCREST<span>SPORTS MEDICINE</span></div></div>
  <div class="slogan__top">BUILDING <em>THE BEST</em></div>
  <div class="slogan__band"></div>
  <div class="slogan__bottom">VERSION OF YOU</div>
</section>

</body>
</html>
```